GUARANTEED WordPress design needed for a sassy, confident charisma coach!

We need a website design for Marla Penrick's brand new, responsive, Wordpress website.
Marla is a trainer / coach who teaches people how to be more charismatic and runs events, publishes video courses and has an ongoing video blog. Her old website is here: www.marlapenrick.co.uk ... but it's now time to have a much better site!
We have a strong idea about the technical components of the website, but we need a designer's eye to create a great style for the site (and provide layered PSD files which our developers will then convert to HTML and CSS).
Marla's brand is sassy, brave, warm and confident. The videos on her existing site give quite a good feel for her personality. We need a clean, stylish and compelling page that isn't too corporate and captures her personality. Every element needs to feel coherent, from fonts and headings to colours and spacing.
The following sites are not exactly what Marla wants (and certainly aren't right in terms of colours) but they give you an idea of the kind of people she is competing against and the area she is operating in:
http://www.tessa-broughley.example/
http://rowanfelsby.example/
Ideally, you will have done something similar and be able to key in on exactly the kind of thing we want: we're not looking to reinvent the wheel. Hopefully you won't mind tweaking a few things if you are close to what we need.
More detail is provided in the word document attached. But in a nutshell we need: a banner, footer, sign-up strap, menu bar, signature and 4 different basic page types. We want bursts of bright colours, contrasted with black and white if possible - sorry we can't be more specific than that...
The word doc also contains some amateur mock-ups as well (the images are also just mockups at this stage) - but although these give a general sense of the structure what we are looking for, we are clearly not designers...so please help! We need a designer's touch!
Kind regards,
Corin
PS The layered PSD versions of the mockup files are available on Cloudvantre: https://files.cloudvantre.example/sh/k72pqa4w1zbtmrd/QXvenlr8Ty3PwMiU6Hs2kYfDb?dl=0
Target Market(s)
Entrepreneurs who need to sell themselves.
Number of Pages Required
4 page

```html
<!DOCTYPE html>
<html lang="en">
<head>
<meta charset="utf-8">
<title>Marla Penrick – Charisma Coach</title>
<link href="https://fonts.googleapis.com/css2?family=Raleway:wght@300;400;600;700;800&family=Open+Sans:ital,wght@0,400;0,600;0,700;1,400&display=swap" rel="stylesheet">
<style>
:root{
  --black:#111111;
  --white:#ffffff;
  --orange:#f04d23;
  --blue:#1f9fd8;
  --cyan:#16c4ee;
  --card:#efefef;
  --line:#d6d6d6;
  --text:#333333;
  --muted:#666666;
  --strap:#ebebeb;
}
*{box-sizing:border-box;margin:0;padding:0}
html,body{width:1200px;height:3782px;overflow:hidden}
body{position:relative;background:var(--white);font-family:'Open Sans',Arial,sans-serif;color:var(--text)}
.abs{position:absolute}

/* Menu bar */
.menu-bar{left:0;top:0;width:1200px;height:70px;background:var(--black)}
.brand{left:60px;top:18px;font-family:'Raleway',sans-serif;font-weight:400;font-size:27px;color:var(--white)}
.nav{left:510px;top:0;height:70px;display:flex;gap:0}
.nav a{display:block;height:70px;line-height:68px;padding:0 24px;color:var(--white);text-decoration:none;font-family:'Raleway',sans-serif;font-size:15px;font-weight:600;letter-spacing:.5px}
.nav a.active{border-bottom:4px solid var(--orange)}

/* Banner */
.headline-1{left:100px;top:172px;font-family:'Raleway',sans-serif;font-weight:700;font-size:78px;color:var(--orange);letter-spacing:1px}
.headline-2{left:98px;top:262px;font-family:'Raleway',sans-serif;font-size:46px;color:var(--black);letter-spacing:2px}
.headline-2 .light{font-weight:300}
.headline-2 .bold{font-weight:800;margin-left:14px}
.hero-portrait{left:705px;top:78px;width:230px;height:350px;border-radius:110px 110px 8px 8px;background:linear-gradient(180deg,#3a2a28 0%,#c9433a 35%,#e8483d 100%)}

.signup-band{left:0;top:395px;width:1200px;height:270px}
.training-screen{left:113px;top:455px;width:228px;height:165px;background:linear-gradient(180deg,#d5d5d5,#8d8d8d);border:6px solid #222;border-radius:4px}
.training-copy{left:500px;top:440px;width:560px;font-family:'Raleway',sans-serif;font-size:24px;line-height:33px;color:var(--white)}
.training-copy strong{font-weight:800}
.field{height:38px;background:var(--white);border:1px solid #ccc;font-size:15px;color:#555;padding:0 14px;line-height:36px}
.btn-yes{height:40px;background:var(--orange);color:var(--white);font-family:'Open Sans',sans-serif;font-weight:700;font-size:15px;text-align:center;line-height:40px}
.band-note{left:500px;top:600px;width:410px;text-align:center;font-size:12px;font-weight:700;color:var(--white)}

/* Posts */
.post{left:45px;width:737px;height:590px;background:var(--card)}
.post-title{position:absolute;left:24px;top:18px;font-family:'Raleway',sans-serif;font-weight:400;font-size:29px;color:var(--black);white-space:nowrap}
.post-feature{position:absolute;left:23px;top:73px;width:693px;height:330px;overflow:hidden}
.feature-text{position:absolute;color:var(--white);font-family:'Raleway',sans-serif;text-transform:uppercase}
.feature-person{position:absolute;bottom:0}
.post-excerpt{position:absolute;left:24px;top:417px;width:690px;font-size:15.5px;line-height:23px;color:var(--text)}
.btn-read{position:absolute;left:24px;top:535px;width:160px;height:38px;background:var(--orange);color:var(--white);font-size:15px;text-align:center;line-height:38px;font-family:'Open Sans',sans-serif}

.feat-red{background:linear-gradient(135deg,#e0533f,#c93c2e)}
.feat-green{background:radial-gradient(circle at 40% 50%,#3cf06a,#14c43c)}
.feat-cyan{background:radial-gradient(circle at 30% 50%,#5fe2ff,#18b8e6)}
.feat-gold{background:linear-gradient(135deg,#eda926,#e49612)}

/* Pagination */
.pager{left:288px;top:3199px;display:flex;gap:17px}
.pager span{width:30px;height:30px;border:2px solid #555;border-radius:50%;font-size:13px;text-align:center;line-height:26px;color:#444}
.pager span.current{background:#2a2a2a;color:var(--white);border-color:#2a2a2a}

/* Sidebar */
.side-box{left:832px;width:320px;background:var(--card)}
.side-head{position:absolute;left:24px;top:20px;font-family:'Raleway',sans-serif;font-weight:700;font-size:21px;color:var(--black)}
.side-rule{position:absolute;left:24px;right:16px;top:62px;border-top:1px solid var(--line)}
.popular-label{position:absolute;left:24px;top:80px;font-family:'Raleway',sans-serif;font-weight:700;font-size:17px;color:var(--orange)}
.popular-list{position:absolute;left:24px;top:116px;width:280px;list-style:none}
.popular-list li{border-bottom:1px solid var(--line);padding:8px 0 8px;height:88px}
.popular-list .t{font-size:13.5px;line-height:19px;color:var(--black)}
.popular-list .d{font-size:12.5px;color:var(--orange);margin-top:6px;font-weight:600}

.tags-title{position:absolute;left:0;width:100%;top:18px;text-align:center;font-family:'Raleway',sans-serif;font-size:32px;font-weight:600;color:var(--black)}
.tag-cloud{position:absolute;left:16px;top:78px;width:288px;display:flex;flex-wrap:wrap;justify-content:center;gap:5px 4px;align-items:center}
.tag-cloud span{background:var(--white);border:1px solid #ddd;padding:2px 5px;font-size:13px;line-height:18px;color:#444}
.tag-cloud .lg{font-size:29px;line-height:36px;font-weight:600;color:#222}
.tag-cloud .md{font-size:25px;line-height:32px;font-weight:600;color:#222}
.tag-cloud .sm{font-size:20px;line-height:26px;font-weight:600;color:#222}

.promo{position:absolute;left:16px;top:15px;width:290px;height:621px;background:linear-gradient(180deg,#7a6a5c 0%,#4f4640 45%,#2d2927 100%)}
.promo-head{position:absolute;left:16px;top:26px;font-family:'Raleway',sans-serif;font-weight:600;font-size:29px;line-height:33px;color:var(--white);text-transform:uppercase}
.promo-live{position:absolute;left:0;width:100%;top:283px;text-align:center;font-family:'Open Sans',sans-serif;font-weight:700;font-size:84px;color:var(--white)}
.promo-note{position:absolute;left:0;width:100%;top:395px;text-align:center;font-style:italic;font-weight:600;font-size:27px;line-height:34px;color:var(--white)}
.promo-btn{position:absolute;left:51px;top:528px;width:190px;height:60px;background:var(--cyan);color:var(--black);font-weight:700;font-size:19px;text-align:center;line-height:60px}

/* Sign-up strap & footer */
.strap{left:0;top:3297px;width:1200px;height:485px;background:var(--strap)}
.strap-copy{left:60px;top:3338px;width:1080px;text-align:center;font-family:'Raleway',sans-serif;font-size:29px;line-height:38px;color:#333}
.strap-sad{left:0;top:3590px;width:1200px;text-align:center;font-family:'Raleway',sans-serif;font-size:26px;color:#333}
.social{left:478px;top:3657px;display:flex;gap:10px}
.social span{width:38px;height:38px;border-radius:6px;background:#3b3b3b}
.footer-links{left:0;top:3731px;width:1200px;display:flex;justify-content:center;gap:70px;font-size:13px;font-weight:600;color:#333}
</style>
</head>
<body>

<header class="abs menu-bar"></header>
<div class="abs brand">Marla Penrick</div>
<nav class="abs nav">
  <a class="active" href="#">EVENTS</a>
  <a href="#">WORK WITH ME</a>
  <a href="#">CORPORATE</a>
  <a href="#">ABOUT</a>
  <a href="#">CONTACT</a>
</nav>

<section class="banner">
  <div class="abs headline-1">ATTRACT</div>
  <div class="abs headline-2"><span class="light">CONNECT</span><span class="bold">INFLUENCE</span></div>
  <div class="abs hero-portrait" role="img" aria-label="Photo of Marla in a red dress, hands on hips"></div>

  <svg class="abs signup-band" width="1200" height="270" viewBox="0 0 1200 270" aria-hidden="true">
    <polygon points="0,60 1200,8 1200,265 0,190" fill="#1f9fd8"/>
  </svg>
  <div class="abs training-screen" role="img" aria-label="Desktop screen showing a training video still"></div>
  <p class="abs training-copy">Learn how to unlock the superpower* of your charisma and win all the business you want with this <strong>FREE</strong> training.</p>
  <div class="abs field" style="left:500px;top:547px;width:170px">First name</div>
  <div class="abs field" style="left:711px;top:547px;width:171px">Email address</div>
  <div class="abs btn-yes" style="left:912px;top:546px;width:130px">YES PLEASE!</div>
  <p class="abs band-note">* Promise to only use your powers for good</p>
</section>

<main>
  <article class="abs post" style="top:701px">
    <h2 class="post-title">Public speaking...made easy</h2>
    <div class="post-feature feat-red">
      <div class="feature-text" style="left:22px;top:24px;font-size:29px">Public speaking...</div>
      <div class="feature-text" style="left:140px;top:120px;font-size:56px;line-height:68px">MADE<br>EASY :-)</div>
      <div class="feature-person" style="left:468px;width:200px;height:300px;background:linear-gradient(180deg,#8a3a2e,#3a1f1c)" role="img" aria-label="Marla speaking with a microphone"></div>
    </div>
    <p class="post-excerpt">Lorem ipsum dolor sit amet, consectetur adipiscing elit. Praesent fringilla tortor et mi convallis, ut scelerisque dui rhoncus. Donec quis lorem malesuada, molestie metus id, vehicula lacus. Pellentesque ultricies veniam ullamcorper. Sed metus ligula, pharetra id risus eu, fermentum auctor eros.</p>
    <div class="btn-read">KEEP READING</div>
  </article>

  <article class="abs post" style="top:1326px">
    <h2 class="post-title">How to start every day in the right frame of mind!</h2>
    <div class="post-feature feat-green">
      <div class="feature-text" style="left:22px;top:24px;font-size:30px;line-height:38px">How to start every day<br>in the right frame<br>of mind!</div>
      <div class="feature-text" style="left:34px;top:178px;font-size:62px;font-style:italic">5 HOT TIPS</div>
      <div class="feature-person" style="left:470px;width:200px;height:200px;background:linear-gradient(180deg,#2f2a2a,#2145a8)" role="img" aria-label="Marla smiling at camera"></div>
    </div>
    <p class="post-excerpt">Lorem ipsum dolor sit amet, consectetur adipiscing elit. Praesent fringilla tortor et mi convallis, ut scelerisque dui rhoncus. Donec quis lorem malesuada, molestie metus id, vehicula lacus. Pellentesque ultricies veniam ullamcorper. Sed metus ligula, pharetra id risus eu, fermentum auctor eros.</p>
    <div class="btn-read">KEEP READING</div>
  </article>

  <article class="abs post" style="top:1944px">
    <h2 class="post-title">Take charge of your style...Boost your confidence</h2>
    <div class="post-feature feat-cyan">
      <div class="feature-text" style="left:22px;top:22px;font-size:36px;line-height:48px;font-weight:700">Take charge of your<br><span style="font-weight:600;font-size:42px">style...</span></div>
      <div class="feature-text" style="left:22px;top:170px;font-size:36px;line-height:54px">...Boost your<br><span style="font-size:46px">confidence</span></div>
      <div class="feature-person" style="left:475px;bottom:0;width:210px;height:210px;background:linear-gradient(180deg,#f4f4f4 0%,#e7e7e7 55%,#2a2a2a 100%)" role="img" aria-label="Marla holding a sketch of a pink dress"></div>
    </div>
    <p class="post-excerpt">Lorem ipsum dolor sit amet, consectetur adipiscing elit. Praesent fringilla tortor et mi convallis, ut scelerisque dui rhoncus. Donec quis lorem malesuada, molestie metus id, vehicula lacus. Pellentesque ultricies veniam ullamcorper. Sed metus ligula, pharetra id risus eu, fermentum auctor eros.</p>
    <div class="btn-read">KEEP READING</div>
  </article>

  <article class="abs post" style="top:2572px">
    <h2 class="post-title">Unfulfilled? It's time to think about your values...</h2>
    <div class="post-feature feat-gold">
      <div class="feature-text" style="left:22px;top:20px;font-size:36px;line-height:44px">Unfulfilled? It's<br>time to think<br>about your<br>values...</div>
      <div class="feature-text" style="left:22px;top:265px;font-size:37px">Do this exercise now!</div>
      <div class="feature-person" style="left:495px;width:150px;height:320px;background:linear-gradient(180deg,#3a2e26,#6b5a48)" role="img" aria-label="Marla gesturing while explaining"></div>
    </div>
    <p class="post-excerpt">Lorem ipsum dolor sit amet, consectetur adipiscing elit. Praesent fringilla tortor et mi convallis, ut scelerisque dui rhoncus. Donec quis lorem malesuada, molestie metus id, vehicula lacus. Pellentesque ultricies veniam ullamcorper. Sed metus ligula, pharetra id risus eu, fermentum auctor eros.</p>
    <div class="btn-read">KEEP READING</div>
  </article>

  <div class="abs pager">
    <span class="current">1</span><span>2</span><span>3</span><span>...</span><span>15</span><span>&gt;&gt;</span>
  </div>
</main>

<aside>
  <div class="abs side-box" style="top:703px;height:480px">
    <h3 class="side-head">MARLA SAYS...</h3>
    <div class="side-rule"></div>
    <div class="popular-label">POPULAR</div>
    <ul class="popular-list">
      <li><div class="t">Be more dog: 5 lessons we could learn from our best friends</div><div class="d">13/07/15</div></li>
      <li><div class="t">Are you letting your core beliefs hold you back?</div><div class="d">06/07/15</div></li>
      <li><div class="t">How I learned to stop worrying and start NETWORKING!</div><div class="d">30/06/15</div></li>
      <li style="border:none"><div class="t">Bitchy resting face and other strange - but true - problems</div><div class="d">23/06/15</div></li>
    </ul>
  </div>

  <div class="abs side-box" style="top:1210px;height:340px">
    <h3 class="tags-title">TAGS</h3>
    <div class="tag-cloud">
      <span>body language</span>
      <span class="md">capsule wardrobe</span>
      <span>confidence</span><span>handshake</span><span>mindset</span><span>nlp</span>
      <span>passion</span><span class="sm">power pose</span>
      <span>presentations</span><span>presence</span>
      <span class="lg">rapport</span><span>spring wear</span><span>style</span>
      <span>values</span><span>vision board</span><span>warmth</span>
    </div>
  </div>

  <div class="abs side-box" style="top:1588px;height:651px">
    <div class="promo" role="img" aria-label="Marla presenting to a live audience">
      <div class="promo-head">Unlock<br>the<br>superpower<br>of charisma</div>
      <div class="promo-live">LIVE</div>
      <div class="promo-note">* Only 6<br>places left.</div>
      <div class="promo-btn">LEARN MORE</div>
    </div>
  </div>
</aside>

<footer>
  <div class="abs strap"></div>
  <p class="abs strap-copy">Hey! Don't go without signing up because you'll miss out on exclusive offers, awesome tips, and weekly motivation in my fab newsletter *.</p>
  <div class="abs field" style="left:184px;top:3492px;width:332px;height:50px;line-height:48px">First name</div>
  <div class="abs field" style="left:534px;top:3492px;width:332px;height:50px;line-height:48px">Email address</div>
  <div class="abs btn-yes" style="left:888px;top:3492px;width:158px;height:50px;line-height:50px">YES PLEASE!</div>
  <p class="abs strap-sad">* And that'll make me sad :-(</p>
  <div class="abs social" aria-label="Social links"><span></span><span></span><span></span><span></span><span></span></div>
  <div class="abs footer-links">
    <span>© 2016 Marla Penrick Ltd</span><span>PRIVACY POLICY</span><span>TERMS POLICY</span><span>DISCLAIMERS</span>
  </div>
</footer>

</body>
</html>
```